Dental Trade Show Brochure

We need a brochure that is created for dental professionals that will explain how our Compliance Management Platform can help them to simplify, centralize and automate their compliance and other documentation requirements for their practices.

would like the content to be refreshed for dental practices. “EHS” should go away, as healthcare has many compliance requirements, not just health and safety. You are the experts. I am looking for your creative genius to help guide me to the right brochure that has text, imagery and design that will speak to my audience.
Updates

Target Market(s)

Dental Industry

Industry/Entity Type

Dental

Requirements
Must have
• would like the content to be refreshed for dental practices. “EHS” should go away, as healthcare has many compliance requirements, not just health and safety. You are the experts. I am looking for your creative genius to help guide me to the right brochure that has text, imagery and design that will speak to my audience.
Nice to have
• We prefer 1 front/back page over bi or tri fold
Should not have
• Other Industry graphics, design, content.

```html
<!DOCTYPE html>
<html lang="en">
<head>
<meta charset="UTF-8">
<title>Clarivo – Dental Compliance Brochure Covers</title>
<link href="https://fonts.googleapis.com/css2?family=Lexend:wght@500;600;700;800&display=swap" rel="stylesheet">
<style>
  :root {
    --backdrop: #d9d9dc;
    --paper: #f2f2f4;
    --navy-deep: #15125a;
    --navy-light: #2b2a86;
    --royal: #2a32d1;
    --royal-bright: #3c4fe8;
    --sky: #b9cdf7;
    --frame-light: #c9daf9;
    --frame-mid: #5f8ff0;
    --brand: #2f5fe0;
    --white: #ffffff;
  }
  html, body {
    margin: 0;
    padding: 0;
    width: 779px;
    height: 1200px;
    overflow: hidden;
    background: var(--backdrop);
  }
  .spread {
    position: absolute;
    top: 307px;
    left: 9px;
    width: 760px;
    height: 585px;
    display: flex;
    box-shadow: 0 6px 24px rgba(0,0,0,0.18);
  }
  .page {
    position: relative;
    width: 380px;
    height: 585px;
    overflow: hidden;
    background: var(--paper);
    font-family: "Lexend", sans-serif;
  }
  .page-art {
    position: absolute;
    inset: 0;
  }
  .brand {
    position: absolute;
    display: flex;
    align-items: center;
    gap: 7px;
  }
  .back-cover .brand { top: 32px; left: 124px; }
  .front-cover .brand { top: 46px; right: 30px; }
  .brand-mark {
    width: 15px;
    height: 15px;
    background: var(--brand);
    border-radius: 2px;
  }
  .brand-name {
    font-weight: 700;
    font-size: 17px;
    color: var(--brand);
    letter-spacing: 0.3px;
  }
  .headline {
    position: absolute;
    top: 376px;
    left: 0;
    width: 380px;
    margin: 0;
    text-align: center;
    font-weight: 800;
    font-size: 22px;
    line-height: 1.1;
    letter-spacing: 0.3px;
  }
  .headline-lead { color: var(--white); display: block; }
  .headline-rest { color: var(--sky); display: block; }
  .site-url {
    position: absolute;
    top: 486px;
    left: 0;
    width: 380px;
    margin: 0;
    text-align: center;
    font-weight: 600;
    font-size: 10px;
    color: var(--white);
    letter-spacing: 0.3px;
  }
  .back-cover .site-url { top: 500px; }
  .contact-list {
    position: absolute;
    top: 392px;
    left: 0;
    width: 380px;
    margin: 0;
    padding: 0;
    list-style: none;
    text-align: center;
    color: var(--white);
    font-weight: 500;
    font-size: 9px;
    line-height: 1.2;
  }
  .contact-item { margin-bottom: 5px; }
  .contact-icon {
    display: block;
    margin: 0 auto 2px;
    width: 10px;
    height: 10px;
  }
</style>
</head>
<body>
<main class="spread">

  <section class="page back-cover">
    <svg class="page-art" width="380" height="585" viewBox="0 0 380 585">
      <defs>
        <linearGradient id="navyBandBack" x1="0" y1="0" x2="1" y2="1">
          <stop offset="0" stop-color="var(--navy-deep)"/>
          <stop offset="1" stop-color="var(--navy-light)"/>
        </linearGradient>
        <linearGradient id="frameBack" x1="0" y1="0" x2="1" y2="1">
          <stop offset="0" stop-color="var(--frame-light)"/>
          <stop offset="0.6" stop-color="var(--frame-mid)"/>
          <stop offset="1" stop-color="var(--frame-light)"/>
        </linearGradient>
        <linearGradient id="photoBack" x1="0" y1="0" x2="1" y2="1">
          <stop offset="0" stop-color="#e3e5ea"/>
          <stop offset="0.5" stop-color="#c9b9b0"/>
          <stop offset="1" stop-color="#9fb3d6"/>
        </linearGradient>
      </defs>
      <path d="M0 225 L380 330 L380 585 L0 585 Z" fill="url(#navyBandBack)"/>
      <path d="M0 225 L380 330 L380 345 L0 242 Z" fill="var(--royal)" opacity="0.55"/>
      <path d="M0 524 C98 510 205 532 380 517 L380 585 L0 585 Z" fill="var(--royal-bright)"/>
      <path d="M0 537 C112 525 224 547 380 535 L380 585 L0 585 Z" fill="var(--royal)"/>
      <polygon points="136,92 244,92 298,190 244,288 136,288 82,190"
        fill="url(#frameBack)" stroke="url(#frameBack)" stroke-width="7" stroke-linejoin="round"/>
      <polygon points="142,101 238,101 287,190 238,279 142,279 93,190"
        fill="url(#photoBack)"
        role="img" aria-label="Photo of a dentist in a mask examining a young girl in the dental chair"/>
    </svg>

    <div class="brand">
      <span class="brand-mark"></span>
      <span class="brand-name">Clarivo</span>
    </div>

    <ul class="contact-list">
      <li class="contact-item">
        <svg class="contact-icon" viewBox="0 0 24 24" fill="none" stroke="var(--white)" stroke-width="2"><path d="M5 3h4l2 5-3 2a12 12 0 0 0 6 6l2-3 5 2v4a2 2 0 0 1-2 2A17 17 0 0 1 3 5a2 2 0 0 1 2-2z"/></svg>
        +1 555-010-2400
      </li>
      <li class="contact-item">
        <svg class="contact-icon" viewBox="0 0 24 24" fill="none" stroke="var(--white)" stroke-width="2"><rect x="3" y="5" width="18" height="14" rx="2"/><path d="M3 7l9 6 9-6"/></svg>
        info@clarivo.cloud
      </li>
      <li class="contact-item">
        <svg class="contact-icon" viewBox="0 0 24 24" fill="none" stroke="var(--white)" stroke-width="2"><path d="M12 22s7-7 7-12a7 7 0 0 0-14 0c0 5 7 12 7 12z"/><circle cx="12" cy="10" r="2.5"/></svg>
        Fairview, CA Lakeside, FL
      </li>
    </ul>

    <p class="site-url">www.clarivo.cloud</p>
  </section>

  <section class="page front-cover">
    <svg class="page-art" width="380" height="585" viewBox="0 0 380 585">
      <defs>
        <linearGradient id="navyBandFront" x1="0" y1="0" x2="1" y2="1">
          <stop offset="0" stop-color="var(--navy-deep)"/>
          <stop offset="1" stop-color="var(--navy-light)"/>
        </linearGradient>
        <linearGradient id="frameFront" x1="0" y1="0" x2="1" y2="1">
          <stop offset="0" stop-color="var(--frame-light)"/>
          <stop offset="0.6" stop-color="var(--frame-mid)"/>
          <stop offset="1" stop-color="var(--frame-light)"/>
        </linearGradient>
        <linearGradient id="photoFront" x1="0" y1="0" x2="1" y2="1">
          <stop offset="0" stop-color="#dfe3e8"/>
          <stop offset="0.55" stop-color="#c8ccd3"/>
          <stop offset="1" stop-color="#b7bcc6"/>
        </linearGradient>
      </defs>
      <path d="M0 263 L380 356 L380 585 L0 585 Z" fill="url(#navyBandFront)"/>
      <path d="M0 263 L380 356 L380 371 L0 280 Z" fill="var(--royal)" opacity="0.55"/>
      <path d="M0 524 C98 510 205 532 380 517 L380 585 L0 585 Z" fill="var(--royal-bright)"/>
      <path d="M0 537 C112 525 224 547 380 535 L380 585 L0 585 Z" fill="var(--royal)"/>
      <polygon points="161,124 283,124 341,229 283,334 161,334 102,229"
        fill="url(#frameFront)" stroke="url(#frameFront)" stroke-width="7" stroke-linejoin="round"/>
      <polygon points="167,134 277,134 331,229 277,324 167,324 113,229"
        fill="url(#photoFront)"
        role="img" aria-label="Photo of a dental hygienist in a face shield treating a smiling patient in the chair"/>
    </svg>

    <div class="brand">
      <span class="brand-mark"></span>
      <span class="brand-name">Clarivo</span>
    </div>

    <h1 class="headline">
      <span class="headline-lead">Optimize Your Business</span>
      <span class="headline-rest">Operations with the</span>
      <span class="headline-rest">Right Tools</span>
    </h1>

    <p class="site-url">www.clarivo.cloud</p>
  </section>

</main>
</body>
</html>
```